K5Lesson WebSite

an educational website about tutoring, client will be surfing this site looking for a tutor, please see the attached images because the contains exactly what we need.
Updates

Project Deadline Extended Reason: something went wrong with the uploaded files, we are very sorry.thank you PixelBazaar for the 5 days extension.now there is a 3 images describing the content of the three pages.good luck Added Friday, August 5, 2016

Target Market(s)

everyone

Industry/Entity Type

Education

Number of Pages Required

3 page

Font styles to use
Other font styles liked:
• something looks good in Arabic and english like "Droid Arabic Kufi"

Requirements
Must have
• the logo we attached, responsive design, simple, also try as much as you can Centering texts and layout because this website will have an Arabic version, Arabic is a Right-to-Left Language.
• a change language button,
Nice to have
• educational gestures.
• Centered texts and layout because this website will have an Arabic version, Arabic is a Right-to-Left Language.
• we have a web designer and we can download any template and add our logo and text to it, but.....
• we need creativity, so please stick to the contents in the images we attached, we need something very simple, more like a varnel home page with little touch of filtering fields like the 5 dropdownlist and the gender selection buttons.
• try not to go far away from the contents we specified in the images, use less images or dont use images at all, try not to make the client scroll down,
Should not have
• too much colors or noisy layout or heavy media

```html
<!DOCTYPE html>
<html lang="en">
<head>
<meta charset="utf-8">
<title>K5Lesson – Find a Tutor</title>
<link href="https://fonts.googleapis.com/css2?family=Roboto+Condensed:wght@400;700&family=Open+Sans:wght@300;400;600;700&display=swap" rel="stylesheet">
<style>
:root{
  --blue:#1b75bc;
  --blue-light:#29a8e0;
  --footer-blue:#1479c4;
  --field-blue:#0f5a98;
  --heading-cyan:#4fd1f3;
  --green:#8dc63f;
  --orange:#f7941d;
  --ink:#231f20;
  --black:#111;
  --frame:#e4e4e4;
  --field:#ececec;
  --white:#fff;
}
*{margin:0;padding:0;box-sizing:border-box}
html,body{width:862px;height:1200px;overflow:hidden;background:var(--frame)}
body{font-family:"Open Sans",sans-serif;color:var(--ink);position:relative}
.page{position:absolute;left:10px;top:10px;width:842px;height:1179px;background:var(--white);overflow:hidden}
.abs{position:absolute}
.cond{font-family:"Roboto Condensed",sans-serif;font-weight:700}

/* header */
.contact-bar{left:410px;top:0;width:432px;height:32px}
.contact-bar .items{position:absolute;left:60px;top:0;height:32px;display:flex;align-items:center;gap:20px;color:var(--white);font-size:11px;font-weight:600}
.contact-bar .item{display:flex;align-items:center;gap:6px}
.socials{display:flex;gap:3px}
.dot{width:14px;height:14px;border:1.5px solid var(--white);border-radius:50%}
.brand{left:22px;top:32px;display:flex;align-items:center;gap:8px}
.brand .mark{width:46px;height:46px;background:var(--blue);border-radius:6px}
.brand .name{font-weight:700;font-size:34px;color:var(--blue);letter-spacing:-0.5px}
.main-nav{left:516px;top:70px;display:flex;align-items:center;gap:16px;font-size:13px}
.main-nav a{color:var(--ink);text-decoration:none}
.main-nav .active{border-bottom:3px solid var(--orange);padding-bottom:2px;margin-top:5px}
.btn-login{background:var(--orange);color:var(--white)!important;width:64px;height:24px;display:flex;align-items:center;justify-content:center;border-radius:2px}
.btn-register{border:1px solid #bbb;width:64px;height:24px;display:flex;align-items:center;justify-content:center;border-radius:3px}
.sub-nav{left:0;top:123px;width:842px;height:36px;background:var(--green);display:flex;justify-content:center;align-items:center;gap:36px;color:var(--white);font-size:12px}

/* hero */
.hero{left:0;top:159px;width:842px;height:359px;background:radial-gradient(ellipse at 55% 40%,#3d5459 0%,#1d2d31 55%,#0c1416 100%)}
.finder{left:45px;top:252px;width:770px;height:191px;background:rgba(13,79,150,.78);border:2px solid var(--white);border-radius:3px}
.finder-icon{left:28px;top:236px}
.finder h1{position:absolute;left:52px;top:16px;font-weight:400;font-size:21px;color:var(--white)}
.btn-listings{position:absolute;left:564px;top:16px;width:182px;height:25px;background:var(--black);color:var(--white);font-size:11px;display:flex;align-items:center;justify-content:center;gap:8px;border-radius:2px}
.form-box{position:absolute;left:10px;top:55px;width:748px;height:123px;background:var(--white);border-radius:3px}
.field{position:absolute;width:237px}
.field label{display:block;font-size:10px;font-weight:600;height:14px;margin-bottom:3px}
.select{height:28px;background:var(--field);font-size:10px;color:#555;padding:0 9px;display:flex;align-items:center;justify-content:space-between;font-weight:600}
.caret{width:0;height:0;border-left:6px solid transparent;border-right:6px solid transparent;border-top:6px solid #444}
.btn-search{position:absolute;left:512px;top:138px;width:237px;height:28px;background:#2a2a2a;color:var(--white);font-size:11.5px;display:flex;align-items:center;justify-content:center;gap:8px;border-radius:2px}

/* steps */
.steps-title{left:0;top:563px;width:842px;text-align:center;font-weight:700;font-size:20px;color:var(--ink)}
.steps-title .b{color:var(--blue)}
.steps-title .o{color:var(--orange)}
.steps-lead{left:0;top:606px;width:842px;text-align:center;font-size:11.5px;font-weight:600}
.step{position:absolute;top:662px;width:180px;text-align:center}
.step-art{width:144px;height:116px;margin:0 auto;background:linear-gradient(90deg,var(--blue-light) 0%,var(--blue-light) 50%,var(--blue) 50%,var(--blue) 100%)}
.step p{font-size:11px;font-weight:600;margin-top:12px;white-space:nowrap}

/* subscribe */
.subscribe{left:0;top:852px;width:842px;height:64px;background:var(--green)}
.subscribe h2{position:absolute;left:77px;top:16px;font-weight:300;font-size:21px;color:var(--white)}
.sub-input{position:absolute;top:16px;width:166px;height:32px;border:1.5px solid var(--white);color:var(--white);font-size:11px;padding:0 12px;display:flex;align-items:center}
.btn-subscribe{position:absolute;left:691px;top:16px;width:75px;height:32px;background:var(--black);color:var(--white);font-size:11px;font-weight:700;display:flex;align-items:center;justify-content:center}

/* footer */
.footer{left:0;top:916px;width:842px;height:238px;background:var(--footer-blue);color:var(--white)}
.footer h3{font-size:12.5px;font-weight:700;color:var(--heading-cyan);padding-bottom:10px;border-bottom:1px solid rgba(255,255,255,.25);margin-bottom:13px;white-space:nowrap}
.footer ul{list-style:none;font-size:10px;font-weight:600;line-height:15.5px;white-space:nowrap}
.f-col{position:absolute;top:37px}
.f-field{position:absolute;left:392px;width:172px;background:var(--field-blue);font-size:8px;font-weight:700;padding:5px 10px}
.btn-submit{position:absolute;left:392px;top:183px;width:76px;height:22px;background:var(--black);font-size:10px;font-weight:700;display:flex;align-items:center;justify-content:center}
.f-brand{position:absolute;left:636px;top:96px;display:flex;align-items:center;gap:8px}
.f-brand .mark{width:42px;height:42px;background:var(--white);border-radius:6px}
.f-brand .name{font-weight:700;font-size:30px}
.bottom{left:0;top:1154px;width:842px;height:25px;background:var(--black);color:var(--white);font-size:8px;font-weight:700;display:flex;align-items:center;justify-content:space-between;padding:0 22px 0 24px}
.bottom .dot{width:14px;height:14px;background:var(--white);border:none}
</style>
</head>
<body>
<div class="page">

  <header>
    <svg class="abs contact-bar" viewBox="0 0 432 32" width="432" height="32"><polygon points="0,0 432,0 405,32 33,32" fill="#1b75bc"/></svg>
    <div class="abs contact-bar">
      <div class="items">
        <span class="item">
          <svg width="16" height="16" viewBox="0 0 16 16"><circle cx="8" cy="8" r="7" fill="none" stroke="#fff" stroke-width="1.3"/><path d="M5.5 4.5l1.5 1.5-1 1c.5 1.2 1.3 2 2.5 2.5l1-1 1.5 1.5-1 1c-2.5-.3-4.6-2.4-5-5z" fill="#fff"/></svg>
          1-800-555-0142</span>
        <span class="item">
          <svg width="16" height="16" viewBox="0 0 16 16"><circle cx="8" cy="8" r="7" fill="none" stroke="#fff" stroke-width="1.3"/><rect x="4.5" y="5.5" width="7" height="5" fill="none" stroke="#fff"/><path d="M4.5 5.5l3.5 3 3.5-3" fill="none" stroke="#fff"/></svg>
          hello@k5lesson.com</span>
        <span class="socials"><span class="dot"></span><span class="dot"></span><span class="dot"></span></span>
      </div>
    </div>

    <div class="abs brand"><span class="mark"></span><span class="name">K5Lesson</span></div>

    <nav class="abs main-nav cond">
      <a class="active" href="#">HOME</a>
      <a href="#">ABOUT</a>
      <a href="#">CONTACT</a>
      <a class="btn-login" href="#">LOGIN</a>
      <a class="btn-register" href="#">REGISTER</a>
    </nav>

    <nav class="abs sub-nav cond">
      <span>SEARCH</span><span>FOR STUDENTS ⌄</span><span>FOR TUTORS ⌄</span><span>FAQ</span><span>RESOURCE</span>
    </nav>
  </header>

  <section class="abs hero" role="img" aria-label="Chalkboard covered in handwritten maths formulas"></section>

  <section class="abs finder">
    <h1>FIND A TUTOR</h1>
    <div class="btn-listings cond">
      <svg width="26" height="16" viewBox="0 0 26 16"><g fill="#fff"><rect x="0" y="1" width="3" height="3"/><rect x="0" y="6.5" width="3" height="3"/><rect x="0" y="12" width="3" height="3"/><rect x="6" y="1" width="20" height="3"/><rect x="6" y="6.5" width="20" height="3"/><rect x="6" y="12" width="20" height="3"/></g></svg>
      VIEW ALL LISTINGS
    </div>
    <div class="form-box">
      <div class="field" style="left:8px;top:13px"><label>SELECT A SUBJECT</label><div class="select">ACADEMIC<span class="caret"></span></div></div>
      <div class="field" style="left:256px;top:13px"><label>LEVEL</label><div class="select">ALL LEVELS<span class="caret"></span></div></div>
      <div class="field" style="left:504px;top:13px"><label>POSTAL CODE</label><div class="select"></div></div>
      <div class="field" style="left:8px;top:70px"><label>SUBJECT DETAIL</label><div class="select">SELECT<span class="caret"></span></div></div>
      <div class="field" style="left:256px;top:70px"><label>TYPE</label><div class="select">ONE ON ONE<span class="caret"></span></div></div>
    </div>
    <div class="btn-search cond">
      <svg width="20" height="16" viewBox="0 0 20 16"><g fill="#fff"><circle cx="5" cy="4" r="2.5"/><circle cx="11" cy="4" r="2.5"/><path d="M0 11c0-3 2-4 5-4s4 1 4 2v2z"/></g><circle cx="14" cy="10" r="3.5" fill="none" stroke="#fff" stroke-width="1.6"/><line x1="16.5" y1="12.5" x2="19.5" y2="15.5" stroke="#fff" stroke-width="1.8"/></svg>
      SEARCH TUTOR
    </div>
  </section>
  <svg class="abs finder-icon" width="56" height="56" viewBox="0 0 56 56"><circle cx="24" cy="24" r="22" fill="#fff"/><circle cx="24" cy="24" r="18" fill="#1b75bc"/><circle cx="22" cy="22" r="9" fill="none" stroke="#fff" stroke-width="4"/><line x1="29" y1="29" x2="44" y2="44" stroke="#fff" stroke-width="6" stroke-linecap="round"/></svg>

  <h2 class="abs steps-title">WE HELP YOU TO FIND <span class="b">A GREAT TUTOR</span> IN <span class="o">4 EASY STEPS!</span></h2>
  <p class="abs steps-lead">K5Lesson.com is a faster, easier way to find a tutor. We have more than 100,000 tutors in 4500 cities all over the world you can contact for FREE!</p>

  <section class="steps">
    <div class="step" style="left:48px">
      <div class="step-art" role="img" aria-label="Open blue book illustration, step 01, with a map pin"></div>
      <p>SEARCH TUTORS IN YOUR AREA</p>
    </div>
    <div class="step" style="left:242px">
      <div class="step-art" role="img" aria-label="Open blue book illustration, step 02, with a star rating"></div>
      <p>READ STUDENT REVIEWS</p>
    </div>
    <div class="step" style="left:436px">
      <div class="step-art" role="img" aria-label="Open blue book illustration, step 03, with a calendar"></div>
      <p>SEE AVAILABILITY</p>
    </div>
    <div class="step" style="left:630px">
      <div class="step-art" role="img" aria-label="Open blue book illustration, step 04, with chat bubbles"></div>
      <p>CONTACT TUTORS FOR FREE!</p>
    </div>
  </section>

  <section class="abs subscribe">
    <h2>Subscribe to our mailing list</h2>
    <div class="sub-input" style="left:345px">Name</div>
    <div class="sub-input" style="left:518px">Email</div>
    <div class="btn-subscribe">SUBSCRIBE</div>
  </section>

  <footer class="abs footer">
    <div class="f-col" style="left:60px;width:96px"><h3>QUICK LINKS</h3>
      <ul><li>SEARCH</li><li>FOR STUDENTS</li><li>FOR TUTORS</li><li>FAQ</li><li>RESOURCE</li><li>LOCATIONS</li><li>ABOUT</li><li>CONTACT</li></ul></div>
    <div class="f-col" style="left:210px;width:110px"><h3>TUTORS</h3>
      <ul><li>BROWSE BY SUBJECT</li><li>BROWSE BY LOCATION</li></ul></div>
    <div class="f-col" style="left:394px;width:172px"><h3>SEND A MESSAGE</h3></div>
    <div class="f-field" style="top:86px;height:21px">NAME</div>
    <div class="f-field" style="top:112px;height:20px">EMAIL</div>
    <div class="f-field" style="top:137px;height:42px">MESSAGE</div>
    <div class="btn-submit">SUBMIT</div>
    <div class="f-brand"><span class="mark"></span><span class="name">K5Lesson</span></div>
  </footer>

  <div class="abs bottom"><span>COPYRIGHT © 2016 K5 LESSON. ALL RIGHTS RESERVED.</span><span class="socials"><span class="dot"></span><span class="dot"></span><span class="dot"></span></span></div>
</div>
</body>
</html>
```